Bill board design For Marlowe’s Construction

Billboard Design Request
Please design the billboard to match the branding, colors, and overall feel of our website: Marlowe's Construction Website
MARLOWE’S CONSTRUCTION
CONCRETE BUILT FOR GENERATIONS
⭐ 5-Star Rated on Zentrop
Please Include:
* All three attached project photos
* Company logo(s)
* Phone Number: 555-014-7723
* Website: MarlowesConstruction-demo.com
* Zentrop logo with 5-star rating graphic
* Pagebloom logo
* Pictavo logo
Service Area:
Kalamazoo • Battle Creek • Coldwater • Grand Rapids
Please arrange the photos and layout in whatever way creates the strongest visual impact and readability from the road. The company name, headline, phone number, and website should be highly visible at highway speeds.
The overall appearance should be clean, professional, premium, and consistent with our website branding while highlighting our reputation, craftsmanship, and quality concrete work.
Target Market(s)
People Driving By
Industry/Entity Type
Concrete Construction

```html
<!DOCTYPE html>
<html lang="en">
<head>
<meta charset="utf-8">
<title>Marlowe’s Construction Billboard</title>
<link rel="stylesheet" href="https://fonts.googleapis.com/css2?family=Montserrat:wght@500;600;700;800&family=Oswald:wght@600&display=swap">
<style>
  :root {
    --board-black: #050505;
    --brand-blue: #2f8fd8;
    --brand-gray: #707070;
    --white: #ffffff;
    --star-gold: #f7b614;
    --page-bg: #e9ecef;
    --garage-top: #8fa46a;
    --garage-bottom: #d9d2c4;
    --crew-top: #6f8a4e;
    --crew-bottom: #3a3128;
    --walk-top: #8a8577;
    --walk-bottom: #a4532f;
  }
  html, body {
    margin: 0;
    width: 1200px;
    height: 828px;
    overflow: hidden;
    background: var(--page-bg);
  }
  .billboard {
    position: absolute;
    left: 20px;
    top: 173px;
    width: 1160px;
    height: 482px;
    display: block;
  }
  .board-bg { fill: var(--board-black); }
  .logo-panel, .service-ribbon { fill: var(--white); }
  .follow-label { font: 600 14px 'Montserrat', sans-serif; fill: var(--white); letter-spacing: 1px; }
  .social-name { font: 600 11px 'Montserrat', sans-serif; fill: var(--white); }
  .logo-name { font: 700 26px 'Montserrat', sans-serif; fill: var(--brand-blue); }
  .brand-blue { font: 800 72px 'Montserrat', sans-serif; fill: var(--brand-blue); }
  .brand-gray { font: 800 60px 'Montserrat', sans-serif; fill: var(--brand-gray); }
  .tagline { font: 600 36px 'Oswald', sans-serif; fill: var(--white); }
  .service-title { font: 800 18px 'Montserrat', sans-serif; fill: var(--brand-blue); }
  .service-list { font: 600 14.5px 'Montserrat', sans-serif; fill: var(--board-black); }
  .rating-name { font: 700 36px 'Montserrat', sans-serif; fill: var(--white); }
  .rating-note { font: 600 14px 'Montserrat', sans-serif; fill: var(--white); }
  .star { fill: var(--star-gold); }
  .phone-number { font: 800 40px 'Montserrat', sans-serif; fill: var(--white); }
  .phone-icon { fill: var(--brand-blue); }
  .web-icon { fill: none; stroke: var(--brand-blue); stroke-width: 2; }
  .website { font: 700 25px 'Montserrat', sans-serif; fill: var(--white); }
</style>
</head>
<body>
<svg class="billboard" viewBox="0 0 1160 482" xmlns="http://www.w3.org/2000/svg">
  <defs>
    <linearGradient id="garagePhoto" x1="0" y1="0" x2="0" y2="1">
      <stop offset="0" stop-color="var(--garage-top)"/>
      <stop offset="0.5" stop-color="#9a6a55"/>
      <stop offset="1" stop-color="var(--garage-bottom)"/>
    </linearGradient>
    <linearGradient id="crewPhoto" x1="0" y1="0" x2="0" y2="1">
      <stop offset="0" stop-color="var(--crew-top)"/>
      <stop offset="1" stop-color="var(--crew-bottom)"/>
    </linearGradient>
    <linearGradient id="walkPhoto" x1="0" y1="0" x2="0" y2="1">
      <stop offset="0" stop-color="var(--walk-top)"/>
      <stop offset="0.4" stop-color="#5d6b3e"/>
      <stop offset="1" stop-color="var(--walk-bottom)"/>
    </linearGradient>
  </defs>

  <rect class="board-bg" width="1160" height="482"/>

  <!-- social -->
  <text class="follow-label" x="47" y="33">FOLLOW US</text>
  <text class="social-name" x="47" y="56">Pagebloom</text>
  <text class="social-name" x="47" y="72">Pictavo</text>

  <!-- logo panel -->
  <polygon class="logo-panel" points="174,4 426,8 351,184 92,182"/>
  <rect x="226" y="52" width="34" height="34" fill="var(--brand-blue)"/>
  <text class="logo-name" x="250" y="125" text-anchor="middle">MARLOWE’S</text>
  <text class="logo-name" x="250" y="155" text-anchor="middle" textLength="190" lengthAdjust="spacingAndGlyphs">CONSTRUCTION</text>

  <!-- project photos -->
  <polygon points="429,11 685,15 595,237 336,232" fill="url(#garagePhoto)" role="img" aria-label="Photo of a new concrete driveway in front of a brick garage"/>
  <polygon points="2,188 344,188 224,473 2,473" fill="url(#crewPhoto)" role="img" aria-label="Photo of a crew member working on a concrete job site"/>
  <polygon points="329,241 588,245 678,477 227,477" fill="url(#walkPhoto)" role="img" aria-label="Photo of a stamped concrete walkway leading to a house"/>

  <!-- headline -->
  <text class="brand-blue" x="699" y="100" textLength="420" lengthAdjust="spacingAndGlyphs">MARLOWE’S</text>
  <text class="brand-gray" x="699" y="152" textLength="422" lengthAdjust="spacingAndGlyphs">CONSTRUCTION</text>
  <text class="tagline" x="701" y="200" textLength="420" lengthAdjust="spacingAndGlyphs">CONCRETE BUILT FOR GENERATIONS</text>

  <!-- service area -->
  <polygon class="service-ribbon" points="701,217 1119,224 1098,257 1121,293 701,288 720,253"/>
  <text class="service-title" x="912" y="243" text-anchor="middle">SERVICE AREA</text>
  <text class="service-list" x="912" y="262" text-anchor="middle">• KALAMAZOO • BATTLE CREEK</text>
  <text class="service-list" x="912" y="281" text-anchor="middle">• COLDWATER • GRAND RAPIDS</text>

  <!-- rating -->
  <text class="rating-name" x="769" y="340" textLength="150" lengthAdjust="spacingAndGlyphs">Zentrop</text>
  <g class="star">
    <polygon points="801,348 803.4,352.6 808.5,353.3 804.8,356.8 805.7,361.8 801,359.4 796.3,361.8 797.2,356.8 793.5,353.3 798.6,352.6"/>
    <polygon points="816,348 818.4,352.6 823.5,353.3 819.8,356.8 820.7,361.8 816,359.4 811.3,361.8 812.2,356.8 808.5,353.3 813.6,352.6"/>
    <polygon points="831,348 833.4,352.6 838.5,353.3 834.8,356.8 835.7,361.8 831,359.4 826.3,361.8 827.2,356.8 823.5,353.3 828.6,352.6"/>
    <polygon points="846,348 848.4,352.6 853.5,353.3 849.8,356.8 850.7,361.8 846,359.4 841.3,361.8 842.2,356.8 838.5,353.3 843.6,352.6"/>
    <polygon points="861,348 863.4,352.6 868.5,353.3 864.8,356.8 865.7,361.8 861,359.4 856.3,361.8 857.2,356.8 853.5,353.3 858.6,352.6"/>
  </g>
  <text class="rating-note" x="932" y="331">5-STAR RATED</text>
  <text class="rating-note" x="932" y="350">ON ZENTROP</text>

  <!-- phone -->
  <path class="phone-icon" transform="translate(-10,0)" d="M760,392 c3,-2 6,-1 7,1 l4,7 c1,2 0,4 -2,5 l-3,2 c2,5 6,9 11,12 l2,-3 c1,-2 3,-2 5,-1 l7,4 c2,1 2,4 1,6 l-3,3 c-3,2 -8,2 -13,-1 c-9,-6 -16,-14 -20,-23 c-2,-5 -1,-9 1,-11 z"/>
  <text class="phone-number" x="790" y="420">555-014-7723</text>

  <!-- website -->
  <g class="web-icon">
    <circle cx="722" cy="448" r="11"/>
    <ellipse cx="722" cy="448" rx="5" ry="11"/>
    <line x1="711" y1="448" x2="733" y2="448"/>
    <line x1="713" y1="442" x2="731" y2="442"/>
    <line x1="713" y1="454" x2="731" y2="454"/>
  </g>
  <text class="website" x="740" y="457" textLength="378" lengthAdjust="spacingAndGlyphs">MarlowesConstruction-demo.com</text>
</svg>
</body>
</html>
```